Distribution/Printing company needs a web site to inform prospective customers on what we do.

Distribution/Printing/Packaging company needs a web site to inform prospective customers on what we do. Please look at our direct to consumer web site (under development) for an idea of the product lines we sell: storedev.kelbrynwares.com
Logo files are attached as is a flyer that is under development which contains other information about the company (this is to be used for content- not to be posted as is). The web site should be focused on our business customer base and is not intended to be direct to consumer. Site should have a link to our consumer web site.
Site design should be mobile friendly, or mobile could be redirected to a mobile version. This web site will be strictly informational and will not be designed for any sales transactions.

Manufacturing and retail businesses, any other multi-site business that would benefit from centralized pricing and budget controls we can provide (banks, medical/dental offices, educational facilities, etc).

• 1) Top level menu: Products, about us, locations, contact us, news
• 2) page with news/promotions that is easily updated
• 3) "contact us" form (name, company, phone, email address) email link
• 4) link to www.store.kelbrynwares.com with information that lower pricing is available for businesses
• 5) SEO keywords
• 6) Link to powerpoint presentation file
• 1) our phone number should appear on every page near the top

```html
<!DOCTYPE html>
<html lang="en">
<head>
<meta charset="utf-8">
<title>Kelbryn Wares – Packaging, Printing, Distribution</title>
<link rel="stylesheet" href="https://fonts.googleapis.com/css2?family=Arimo:wght@400;700&family=Jost:wght@400;500&display=swap">
<style>
:root{
  --brand-blue:#4a87aa;
  --brand-dark:#2b6f90;
  --text-dark:#111;
  --text-body:#555;
  --text-muted:#6a6a6a;
  --link-blue:#2a6f99;
  --hero-bg:#e8eef2;
  --white:#fff;
  --band:#f1f1f1;
}
*{box-sizing:border-box;margin:0;padding:0}
html,body{width:997px;height:1200px;overflow:hidden;background:var(--white)}
body{position:relative;font-family:"Arimo",Arial,sans-serif;color:var(--text-dark)}
.abs{position:absolute}
.top-bar{left:84px;top:0;width:830px;height:7px;background:var(--brand-dark);border-radius:0 0 6px 6px}
.quick-call{left:97px;top:44px;font-size:11.5px;color:#000}
.quick-call a{font-style:italic;color:var(--link-blue);font-size:12.5px;text-decoration:none;margin-left:3px}
.lang-select{left:735px;top:44px;width:166px;height:19px;border:1px solid #b8c7d2;background:linear-gradient(#f5f8fa,#dfe8ee);font-size:11px;padding:3px 6px;color:#111}
.lang-select span{position:absolute;right:2px;top:2px;width:15px;height:13px;background:#222}
.lang-select span::after{content:"";position:absolute;left:4px;top:4px;border:4px solid transparent;border-top:5px solid #fff}
.brand{left:94px;top:72px;width:200px}
.brand-name{font-family:"Jost",sans-serif;font-weight:500;font-size:21px;letter-spacing:.5px;color:#111;display:flex;align-items:center;gap:8px}
.brand-name i{display:inline-block;width:12px;height:12px;background:#111}
.brand-tag{font-size:11.5px;color:#111;margin-top:6px;font-weight:700;letter-spacing:.2px}
.main-nav{left:390px;top:115px;display:flex;font-size:12.5px;color:#000}
.main-nav a{color:#000;text-decoration:none;position:absolute;white-space:nowrap}
.hero{left:0;top:161px;width:997px;height:338px;background:linear-gradient(180deg,#f4f7f9 0%,var(--hero-bg) 60%,#dfe7ec 100%)}
.hero-photo{left:85px;top:170px;width:560px;height:318px;background:radial-gradient(ellipse at 40% 55%,#b99a74 0%,#cdb497 35%,rgba(220,228,233,0) 72%)}
.hero-copy{left:675px;top:280px;font-family:"Jost",sans-serif;font-size:21.5px;line-height:30.5px;color:#4a4a4a}
.hero-btn{left:675px;top:411px;width:124px;height:33px;background:var(--brand-blue);border-radius:3px;color:var(--white);font-family:"Jost",sans-serif;font-size:15.5px;display:flex;align-items:center;justify-content:center}
.dots{left:452px;top:509px;display:flex;gap:5px}
.dots i{width:12px;height:12px;border-radius:50%;border:1px solid #999;background:var(--white)}
.dots i.on{background:#555;border-color:#555}
.services-band{left:0;top:499px;width:997px;height:263px;background:linear-gradient(180deg,#fff 60%,var(--band) 100%)}
.service{width:230px}
.service-icon{width:78px;height:74px;border-radius:8px}
.service h3{font-weight:400;font-size:16px;color:var(--link-blue);margin:14px 0 12px 2px}
.service p{font-size:11px;line-height:16.6px;color:var(--text-body)}
.service a{display:inline-block;margin-top:15px;font-size:11px;color:var(--link-blue)}
.enquiry{left:107px;top:786px;width:783px;height:170px;background:var(--brand-blue);border-radius:3px}
.enquiry-copy{left:15px;top:15px;width:310px;font-family:"Jost",sans-serif;font-size:15.5px;line-height:18.2px;color:var(--white)}
.enquiry-copy p+p{margin-top:18px}
.field{background:var(--white);font-size:12px;color:#9a9a9a;padding:7px 13px}
.send{left:361px;top:135px;color:var(--white);font-size:15px;text-decoration:underline}
.site-footer{left:0;top:975px;width:997px}
.foot-brand{left:104px;top:10px}
.foot-brand .brand-name{font-size:12px;gap:5px}
.foot-brand .brand-name i{width:7px;height:7px}
.foot-brand small{display:block;font-size:7px;font-weight:700;margin-top:2px}
.foot-address{left:104px;top:72px;font-size:10.5px;line-height:15px;color:var(--text-muted)}
.foot-col h4{font-family:"Jost",sans-serif;font-weight:400;font-size:16px;color:#111;letter-spacing:.3px}
.foot-col ul{list-style:none;margin-top:15px;font-size:10.5px;line-height:15px;color:var(--text-muted)}
.blog-head{margin-top:15px;font-size:10.5px;font-weight:700;color:#666;letter-spacing:.3px}
.blog-text{font-size:10.5px;line-height:12.5px;color:var(--text-muted);width:130px}
.social{display:flex;gap:9px;margin-top:28px;margin-left:3px}
.social i{width:21px;height:21px;border-radius:50%;background:var(--link-blue)}
</style>
</head>
<body>
<div class="abs top-bar"></div>

<header>
  <p class="abs quick-call">For Quick response u can call us at: <a href="tel:0205550187">020 555 0187</a></p>
  <div class="abs lang-select">Select Language<span></span></div>
  <div class="abs brand">
    <div class="brand-name"><i></i>KELBRYN WARES</div>
    <div class="brand-tag">Packaging • Printing • Distribution</div>
  </div>
  <nav class="abs main-nav">
    <a style="left:0;top:0">Packaging</a>
    <a style="left:83px;top:0">Office Supplies</a>
    <a style="left:191px;top:0">Janitorial</a>
    <a style="left:266px;top:0">Retail Supplies</a>
    <a style="left:376px;top:0">About Us</a>
    <a style="left:453px;top:0">Contact US</a>
  </nav>
</header>

<section class="abs hero"></section>
<div class="abs hero-photo" role="img" aria-label="Photo of printed cardboard product boxes"></div>
<p class="abs hero-copy">See how we provide<br>innovative services to<br>your business with<br>economical price</p>
<a class="abs hero-btn">Contact Us Now</a>

<section class="abs services-band"></section>
<div class="abs dots"><i class="on"></i><i></i><i></i><i></i></div>

<article class="abs service" style="left:111px;top:532px">
  <div class="service-icon" role="img" aria-label="Magnifying glass over a chart icon" style="background:radial-gradient(circle at 30% 35%,#d9eef5 0 30%,#7a8a90 31% 40%,transparent 42%)"></div>
  <h3>Packaging</h3>
  <p>some lorem ipsum text will be here some lorem ipsum text will be here some lorem ipsum text will be here some lorem ipsum text will be here some lorem ipsum text will be here</p>
  <a>read more</a>
</article>
<article class="abs service" style="left:395px;top:532px">
  <div class="service-icon" role="img" aria-label="Silhouette head with marketing words illustration" style="width:56px;background:#1c1c1c;border-radius:40% 40% 20% 30%"></div>
  <h3>Printing</h3>
  <p>some lorem ipsum text will be here some lorem ipsum text will be here some lorem ipsum text will be here some lorem ipsum text will be here some lorem ipsum text will be here</p>
  <a>read more</a>
</article>
<article class="abs service" style="left:670px;top:534px">
  <div class="service-icon" role="img" aria-label="Folder with documents icon" style="background:linear-gradient(160deg,#e9b14d,#c7801c)"></div>
  <h3 style="margin-top:16px">Distribution</h3>
  <p>some lorem ipsum text will be here some lorem ipsum text will be here some lorem ipsum text will be here some lorem ipsum text will be here some lorem ipsum text will be here</p>
  <a>read more</a>
</article>

<section class="abs enquiry">
  <div class="abs enquiry-copy">
    <p>Are your looking for marketing service for your business, Just fill the form and we will get back to you as soon as possible.</p>
    <p>Our mission is to build image of the client's company and increase awareness of their products to improve their competitiveness and innovativeness.</p>
  </div>
  <div class="abs field" style="left:360px;top:29px;width:187px;height:28px">Your Name</div>
  <div class="abs field" style="left:561px;top:29px;width:187px;height:28px">Your Email id</div>
  <div class="abs field" style="left:361px;top:70px;width:387px;height:56px">Message</div>
  <a class="abs send">Send</a>
</section>

<footer class="abs site-footer">
  <div class="abs foot-brand">
    <div class="brand-name"><i></i>KELBRYN WARES</div>
    <small>Packaging • Printing • Distribution</small>
  </div>
  <p class="abs foot-address">Harrowgate Trade Ltd.<br>48, Alder Row,<br>Leeds<br>UK<br>Call: 020 555 0187</p>
  <div class="abs foot-col" style="left:306px;top:33px">
    <h4>ABOUT US</h4>
    <ul><li>About Us</li><li>Careers</li><li>For the Press</li><li>Terms of Use</li><li>Privacy</li></ul>
  </div>
  <div class="abs foot-col" style="left:456px;top:33px">
    <h4>SERVICES</h4>
    <ul><li>Services details</li><li>Services details here</li><li>Services details</li><li>Services details</li><li>here details</li><li>Services details</li><li>Services details</li></ul>
  </div>
  <div class="abs foot-col" style="left:615px;top:33px">
    <h4>BLOG</h4>
    <p class="blog-head">Latest Articles heading</p>
    <p class="blog-text">some text will be here some text will be here some text will be here some text will be here some text will be here</p>
  </div>
  <div class="abs foot-col" style="left:807px;top:33px">
    <h4>FOLLOW US</h4>
    <div class="social"><i></i><i></i><i></i></div>
  </div>
</footer>
</body>
</html>
```